Redesign website

I purchased a business a few months ago and I'm in the process on rebranding everything and creating a new website. I want the new website completely different with 5 pages and nice pictures on every page. Also I want my new logo and colors to included on the site.
Current Site https://www.bristlewoodpetsinc.com

Industry/Entity Type

Dog Sitting

Coding

Coded - Design and coding required

Number of Pages Required

5+ page

Requirements
Must have
• I have pictures and a video I can shared to use for the website.
Just as the current site it should have an option to be taken to the site I have to make reservations.
Nice to have
• Would be nice to have social media intergrations

```html
<!DOCTYPE html>
<html lang="en">
<head>
<meta charset="utf-8">
<title>Bristlewood Pets – Pet Boarding & Daycare</title>
<link href="https://fonts.googleapis.com/css2?family=Montserrat:wght@400;600;700;800&family=Open+Sans:wght@400;600;700&display=swap" rel="stylesheet">
<style>
:root{
  --teal:#1db3bf;
  --teal-dark:#1596a0;
  --magenta:#c0177a;
  --ink:#333;
  --muted:#666;
  --grey-bg:#ececec;
  --footer:#1f1f1f;
  --footer-base:#161616;
  --white:#fff;
}
*{box-sizing:border-box;margin:0;padding:0}
html,body{width:1200px;height:3336px;overflow:hidden}
body{font-family:"Open Sans",sans-serif;color:var(--ink);background:var(--white);position:relative}
.abs{position:absolute}
.photo{position:absolute}
h2.section-title{font-family:"Montserrat",sans-serif;font-weight:600;font-size:30px;line-height:36px;text-align:center;color:#222;letter-spacing:1px}
.rule{width:60px;height:3px;background:var(--magenta);margin:10px auto 0}
.btn{display:inline-block;font-family:"Montserrat",sans-serif;font-weight:700;font-size:14px;letter-spacing:1px;color:#fff;padding:12px 22px;text-transform:uppercase}
.btn-teal{background:var(--teal)}
.btn-magenta{background:var(--magenta)}

/* header */
.site-header{position:absolute;top:0;left:0;width:1200px;height:112px;background:#fff}
.brand{position:absolute;left:120px;top:14px;display:flex;align-items:center;gap:12px}
.brand-mark{width:24px;height:24px;border-radius:50%;background:var(--magenta)}
.brand-name{font-family:"Montserrat",sans-serif;font-weight:700;font-size:24px;color:var(--teal)}
.follow{position:absolute;left:680px;top:18px;display:flex;align-items:center;gap:10px;font-family:"Montserrat",sans-serif;font-size:13px;font-weight:700;color:#333}
.follow span.dot{width:28px;height:28px;border-radius:50%;background:var(--teal-dark)}
.call{position:absolute;left:930px;top:10px;display:flex;gap:10px;align-items:center}
.call .ic{width:36px;height:36px;border-radius:50%;background:var(--magenta);display:flex;align-items:center;justify-content:center}
.call small{display:block;font-size:11px;font-weight:700;color:#555}
.call strong{font-family:"Montserrat",sans-serif;font-size:28px;color:var(--teal);font-weight:700}
.main-nav{position:absolute;left:530px;top:74px;display:flex;gap:34px;font-family:"Montserrat",sans-serif;font-size:14px;font-weight:600;color:#333}
.main-nav .active{color:var(--magenta);border-bottom:2px solid var(--magenta);padding-bottom:4px}

/* hero */
.hero{position:absolute;top:112px;left:0;width:1200px;height:548px;
  background:
    radial-gradient(ellipse 260px 220px at 560px 230px,rgba(245,242,232,.85),rgba(245,242,232,0) 70%),
    radial-gradient(ellipse 160px 130px at 980px 390px,rgba(60,140,200,.7),rgba(60,140,200,0) 70%),
    linear-gradient(180deg,#5d5a4a 0%,#6f7a55 30%,#7fa04a 55%,#5f8a2c 100%)}
.hero-title{position:absolute;left:120px;top:180px;font-family:"Montserrat",sans-serif;font-weight:800;font-size:50px;line-height:60px;color:#fff;letter-spacing:1px}
.hero .btn{position:absolute;left:120px;top:420px}
.hero-dots{position:absolute;left:570px;top:500px;display:flex;gap:8px}
.hero-dots i{width:10px;height:10px;border-radius:50%;background:rgba(255,255,255,.6)}
.hero-dots i.on{background:#fff}

/* welcome */
.welcome{position:absolute;top:660px;left:0;width:1200px;height:460px}
.welcome-photo{position:absolute;left:160px;top:40px;width:290px;height:290px;border-radius:50%;border:6px solid var(--teal);background:radial-gradient(circle at 50% 45%,#c58a58,#9a6338 55%,#5a3a22 100%)}
.welcome-copy{position:absolute;left:620px;top:50px;width:440px}
.welcome-copy h3{font-family:"Montserrat",sans-serif;font-weight:700;font-size:22px;color:#222;line-height:30px}
.welcome-copy .rule{margin:8px 0 16px}
.welcome-copy p{font-size:12.5px;line-height:19px;color:var(--muted)}
.welcome-copy .btn{margin-top:26px}

/* services */
.services{position:absolute;top:1120px;left:0;width:1200px;height:950px;background:var(--grey-bg)}
.services h2{position:absolute;top:48px;width:100%}
.service-card{position:absolute;background:var(--teal);color:#fff;padding:30px 30px}
.service-card h4{font-family:"Montserrat",sans-serif;font-weight:700;font-size:19px;letter-spacing:.5px}
.service-card .rule{margin:8px 0 22px;background:var(--magenta)}
.service-card p{font-size:16px;line-height:25px}
.service-card p.small{font-size:13px;line-height:20px}
.service-card .btn{padding:8px 14px;font-size:11px;margin-top:16px}

/* gallery */
.gallery{position:absolute;top:2070px;left:0;width:1200px;height:450px}
.gallery h2{position:absolute;top:22px;width:100%}
.thumb{position:absolute;top:112px;width:236px;height:230px}
.arrow{position:absolute;top:214px;width:28px;height:28px;border-radius:50%;background:#fff;box-shadow:0 1px 4px rgba(0,0,0,.3);display:flex;align-items:center;justify-content:center}
.gallery .btn{position:absolute;left:525px;top:374px;padding:10px 18px;font-size:12px}

/* reservation */
.reservation{position:absolute;top:2520px;left:0;width:1200px;height:470px;background:linear-gradient(90deg,#18a9b5 0%,#1db3bf 55%,#2bbcc6 100%)}
.reservation-photo{position:absolute;left:620px;top:0;width:580px;height:470px;background:radial-gradient(ellipse 220px 180px at 340px 260px,rgba(15,90,96,.55),rgba(15,90,96,0) 75%),linear-gradient(90deg,rgba(29,179,191,0),rgba(20,120,128,.5))}
.reservation h3{position:absolute;left:120px;top:40px;font-family:"Montserrat",sans-serif;font-weight:600;font-size:26px;color:#fff;letter-spacing:1px}
.reservation .line{position:absolute;left:120px;top:84px;width:520px;height:1px;background:rgba(255,255,255,.6)}
.field{position:absolute;background:#fff;font-size:11px;font-weight:700;color:#333;padding:14px 12px;height:48px}
.reservation .btn{position:absolute;left:120px;top:372px;padding:10px 18px;font-size:13px}

/* footer */
.site-footer{position:absolute;top:2990px;left:0;width:1200px;height:310px;background:var(--footer);color:#ccc}
.footer-brand{position:absolute;left:140px;top:120px;display:flex;align-items:center;gap:12px}
.footer-col{position:absolute;top:42px;font-size:13px;line-height:20px}
.footer-col h5{font-family:"Montserrat",sans-serif;font-size:14px;font-weight:700;color:#fff;margin-bottom:14px;letter-spacing:1px}
.ci{display:flex;gap:12px;margin-bottom:14px;align-items:flex-start}
.ci .c{width:30px;height:30px;border-radius:50%;background:#fff;flex:none;display:flex;align-items:center;justify-content:center}
.copyright{position:absolute;top:3300px;left:0;width:1200px;height:36px;background:var(--footer-base);color:#888;font-size:11px;text-align:center;line-height:36px}
</style>
</head>
<body>

<header class="site-header">
  <div class="brand"><span class="brand-mark"></span><span class="brand-name">Bristlewood Pets</span></div>
  <div class="follow">FOLLOW US <span class="dot"></span><span class="dot"></span><span class="dot"></span><span class="dot"></span></div>
  <div class="call">
    <div class="ic"><svg width="18" height="18" viewBox="0 0 24 24"><path fill="#fff" d="M6.6 10.8a15 15 0 006.6 6.6l2.2-2.2c.3-.3.7-.4 1-.2 1.1.4 2.3.6 3.6.6.6 0 1 .4 1 1V20c0 .6-.4 1-1 1A17 17 0 013 4c0-.6.4-1 1-1h3.5c.6 0 1 .4 1 1 0 1.3.2 2.5.6 3.6.1.3 0 .7-.2 1z"/></svg></div>
    <div><small>CALL US NOW</small><strong>(555) 014 2290</strong></div>
  </div>
  <nav class="main-nav"><span class="active">HOME</span><span>ABOUT</span><span>SERVICES</span><span>PHOTOS</span><span>POLICIES</span><span>CONTACT</span></nav>
</header>

<section class="hero" role="img" aria-label="Small white terrier running across a grassy lawn">
  <h1 class="hero-title">PET BOARDING<br>&amp; DAYCARE</h1>
  <span class="btn btn-teal">Read More</span>
  <div class="hero-dots"><i class="on"></i><i></i><i></i><i></i><i></i></div>
</section>

<section class="welcome">
  <div class="welcome-photo" role="img" aria-label="Fluffy brown doodle dog portrait"></div>
  <span class="abs" style="left:150px;top:80px;width:22px;height:22px;border-radius:50%;background:var(--magenta)"></span>
  <span class="abs" style="left:432px;top:60px;width:16px;height:16px;border-radius:50%;background:var(--magenta)"></span>
  <span class="abs" style="left:420px;top:300px;width:26px;height:26px;border-radius:50%;background:var(--magenta)"></span>
  <span class="abs" style="left:200px;top:318px;width:14px;height:14px;border-radius:50%;background:var(--teal)"></span>
  <div class="welcome-copy">
    <h3>WELCOME TO<br>BRISTLEWOOD PETS</h3>
    <div class="rule"></div>
    <p>Bristlewood Pets' mission is to provide gentle, loving care for your pets in a fun and friendly environment in a way that allows you, the pet owner, to worry less about your companion while you are away. We want to create a stress-free environment for our furry guests and a fun, playful atmosphere for our employees. A tired pup is a happy pup. That is why we have provided several indoor and outdoor play areas to stimulate your pup to the point he doesn't have time to miss you. You can rest assured your furbaby will have plenty of playful socialization throughout the day.</p>
    <span class="btn btn-teal">Read More</span>
  </div>
</section>

<section class="services">
  <h2 class="section-title">OUR SERVICES<div class="rule"></div></h2>
  <div class="service-card" style="left:140px;top:130px;width:420px;height:360px">
    <h4>DOGGIE DAYCARE</h4><div class="rule"></div>
    <p>Full Day - $20</p>
    <p>Half Day (&lt;4 Hrs)- $15</p>
    <p style="margin-top:12px">Discount packages:</p>
    <p class="small">10 Full-Day visits (do not expire) $160<br>20 Half-Day visits (do not expire) $270</p>
    <span class="btn btn-magenta">Reserve</span>
  </div>
  <div class="photo" role="img" aria-label="Man playing with several dogs in a fenced yard" style="left:560px;top:130px;width:510px;height:360px;background:radial-gradient(ellipse 200px 80px at 330px 250px,rgba(40,35,30,.55),rgba(40,35,30,0) 75%),linear-gradient(180deg,#4f5a3c 0%,#6b5a45 35%,#7a9a4e 60%,#6e9140 100%)"></div>
  <div class="photo" role="img" aria-label="Curly doodle puppy walking on grass" style="left:140px;top:520px;width:520px;height:360px;background:radial-gradient(ellipse 130px 110px at 250px 180px,rgba(205,160,110,.85),rgba(205,160,110,0) 75%),linear-gradient(180deg,#5a4a3c 0%,#6b5a45 25%,#7fa04e 50%,#6a8f3a 100%)"></div>
  <div class="service-card" style="left:660px;top:520px;width:410px;height:360px">
    <h4>OVERNIGHT BOARDING</h4><div class="rule"></div>
    <p class="small" style="font-size:14px">Dog Boarding INCLUDES off leash play in our daycare (a $20/day value).</p>
    <p class="small" style="font-size:14px;margin-top:16px">1st Dog - $40/night<br>2 Dogs/same kennel - $55/night<br>Each Add'l Dog/Same kennel - $15/night</p>
    <span class="btn btn-magenta">Reserve</span>
  </div>
</section>

<section class="gallery">
  <h2 class="section-title">GALLERY<div class="rule"></div></h2>
  <div class="thumb" role="img" aria-label="Dogs resting in a kennel" style="left:130px;background:radial-gradient(ellipse 90px 70px at 120px 130px,rgba(120,80,50,.7),rgba(120,80,50,0) 75%),linear-gradient(#8a6a55,#c8aa90)"></div>
  <div class="thumb" role="img" aria-label="Two white dogs posing together" style="left:372px;background:radial-gradient(ellipse 100px 80px at 118px 140px,rgba(245,243,238,.95),rgba(245,243,238,0) 75%),linear-gradient(#8fa8b8,#cfc8bc)"></div>
  <div class="thumb" role="img" aria-label="Beagle sitting on a blue floor" style="left:614px;background:radial-gradient(ellipse 80px 100px at 118px 110px,rgba(170,110,55,.9),rgba(170,110,55,0) 75%),linear-gradient(#2e63b5,#3a6fc0)"></div>
  <div class="thumb" role="img" aria-label="Dog lying on a bed" style="left:856px;width:214px;background:radial-gradient(ellipse 90px 70px at 110px 140px,rgba(150,110,80,.6),rgba(150,110,80,0) 75%),linear-gradient(#6b5145,#3d2f2a)"></div>
  <div class="arrow" style="left:112px"><svg width="10" height="10" viewBox="0 0 10 10"><path d="M7 1L3 5l4 4" stroke="#333" stroke-width="2" fill="none"/></svg></div>
  <div class="arrow" style="left:1058px"><svg width="10" height="10" viewBox="0 0 10 10"><path d="M3 1l4 4-4 4" stroke="#333" stroke-width="2" fill="none"/></svg></div>
  <span class="btn btn-magenta">View All Images</span>
</section>

<section class="reservation">
  <div class="reservation-photo" role="img" aria-label="Dog lying down, tinted in teal"></div>
  <h3>RESERVATION</h3>
  <div class="line"></div>
  <div class="field" style="left:120px;top:120px;width:250px">NAME</div>
  <div class="field" style="left:390px;top:120px;width:250px">E-MAIL</div>
  <div class="field" style="left:120px;top:184px;width:250px">PHONE</div>
  <div class="field" style="left:390px;top:184px;width:250px">SUBJECT</div>
  <div class="field" style="left:120px;top:248px;width:520px;height:100px">MESSAGE</div>
  <span class="btn btn-magenta">Submit</span>
</section>

<footer class="site-footer">
  <div class="footer-brand"><span class="brand-mark"></span><span class="brand-name">Bristlewood Pets</span></div>
  <div class="footer-col" style="left:470px">
    <h5>MENU</h5>
    HOME<br>ABOUT<br>SERVICES<br>PHOTOS<br>POLICIES<br>CONTACT
  </div>
  <div class="footer-col" style="left:670px;width:230px">
    <h5>CONTACT US</h5>
    <div class="ci"><span class="c"><svg width="12" height="14" viewBox="0 0 12 16"><path fill="#333" d="M6 0a6 6 0 00-6 6c0 4.5 6 10 6 10s6-5.5 6-10a6 6 0 00-6-6zm0 8.5A2.5 2.5 0 116 3.5a2.5 2.5 0 010 5z"/></svg></span><span>2140 Meadow Lane Road<br>Riverside, GA 30100</span></div>
    <div class="ci"><span class="c"><svg width="12" height="12" viewBox="0 0 24 24"><path fill="#333" d="M6.6 10.8a15 15 0 006.6 6.6l2.2-2.2c.3-.3.7-.4 1-.2 1.1.4 2.3.6 3.6.6.6 0 1 .4 1 1V20c0 .6-.4 1-1 1A17 17 0 013 4c0-.6.4-1 1-1h3.5c.6 0 1 .4 1 1 0 1.3.2 2.5.6 3.6.1.3 0 .7-.2 1z"/></svg></span><span>Call Us<br>(555) 014 2290</span></div>
    <div class="ci"><span class="c"><svg width="14" height="10" viewBox="0 0 14 10"><rect x="0.5" y="0.5" width="13" height="9" fill="none" stroke="#333"/><path d="M1 1l6 5 6-5" fill="none" stroke="#333"/></svg></span><span>E-mail Us<br>hello@bristlewoodpets.com</span></div>
  </div>
  <div class="footer-col" style="left:930px">
    <h5>FOLLOW US</h5>
    <div class="ci"><span class="c"></span><span>Like us on<br>our page</span></div>
    <div class="ci"><span class="c"></span><span>Follow us on<br>our feed</span></div>
    <div class="ci"><span class="c"></span><span>Follow us on<br>our gallery</span></div>
  </div>
</footer>
<div class="copyright">Copyright © 2018 All Rights Reserved</div>

</body>
</html>
```